Poster of Core Values & Motto

Create our core values poster and motto. Attached are our core values and our Motto. This poster represents both of our companies Tidal Pulp & CarvoBin.

Target Market(s)

Our team / employees

Industry/Entity Type

Shredding and Medical Waste

Colors
59FF00
82FF00
B8FF75
E3FFCB
F4FFEA
EB3D1F
EC4F4E
F09395
F8D3D4
FCEDEE

Requirements
Must have
• Include both companies logos

```html
<!DOCTYPE html>
<html lang="en">
<head>
<meta charset="utf-8">
<title>Core Values Poster</title>
<link href="https://fonts.googleapis.com/css2?family=Poppins:wght@400;500;600;700&display=swap" rel="stylesheet">
<style>
  :root {
    --page: #d9d9d9;
    --red: #d21f26;
    --red-deep: #b3161d;
    --red-soft: #ec4f4e;
    --green: #2ba84a;
    --green-bright: #3cb44b;
    --ink: #1c1c1c;
    --sky: #cfe2f3;
    --white: #ffffff;
  }
  * { margin: 0; padding: 0; box-sizing: border-box; }
  html, body { width: 1200px; height: 1200px; overflow: hidden; background: var(--page); }
  body { font-family: "Poppins", sans-serif; color: var(--ink); }

  .poster {
    position: absolute; left: 220px; top: 46px;
    width: 760px; height: 1108px;
    background: var(--white);
    overflow: hidden;
  }

  /* Header */
  .header {
    position: absolute; left: 0; top: 0; width: 760px; height: 403px;
    background: linear-gradient(180deg, #c41b22 0%, var(--red) 45%, #d8242a 100%);
  }
  .header-photo {
    position: absolute; left: 418px; top: 14px; width: 270px; height: 378px;
    background: radial-gradient(ellipse at 50% 55%, #e0343a 0%, #cf2228 60%, rgba(210,31,38,0) 100%);
  }
  .motto {
    position: absolute; left: 63px; top: 66px;
    color: var(--white); font-weight: 700; font-size: 68px; line-height: 67px; letter-spacing: 2px;
  }
  .tagline {
    position: absolute; left: 71px; top: 272px;
    color: var(--white); font-weight: 500; font-size: 38px; line-height: 47px; letter-spacing: 1.5px;
  }

  /* Values area */
  .values {
    position: absolute; left: 0; top: 403px; width: 760px; height: 585px;
    background:
      radial-gradient(ellipse 320px 160px at 400px 60px, rgba(150,195,235,0.55), rgba(255,255,255,0) 100%),
      radial-gradient(ellipse 260px 200px at 640px 240px, rgba(180,210,238,0.45), rgba(255,255,255,0) 100%),
      linear-gradient(180deg, #eef4fa 0%, #f7f9fb 60%, #fdfdfd 100%);
  }
  .value-icon { position: absolute; width: 82px; height: 82px; }
  .value-title {
    position: absolute; font-weight: 600; font-size: 20px; letter-spacing: 1px; white-space: nowrap;
  }
  .value-note {
    position: absolute; font-size: 12.5px; line-height: 14px; letter-spacing: 0.6px; color: #333;
  }

  .core-badge { position: absolute; left: 253px; top: 161px; width: 254px; height: 280px; }
  .core-label {
    position: absolute; left: 253px; top: 228px; width: 254px; text-align: center;
    color: var(--white); font-weight: 700; font-size: 53px; line-height: 52px; letter-spacing: 2px;
  }

  /* Footer */
  .divider { position: absolute; left: 0; top: 988px; width: 760px; height: 5px; background: var(--ink); }
  .footer { position: absolute; left: 0; top: 993px; width: 760px; height: 115px; background: var(--white); }
  .brand {
    position: absolute; top: 34px; font-weight: 700; font-size: 34px; letter-spacing: 1px;
  }
  .brand-carvobin { left: 57px; color: var(--red); }
  .brand-tidal { left: 476px; color: var(--green); display: flex; align-items: center; gap: 12px; }
  .brand-tidal .dot { width: 30px; height: 30px; border-radius: 50%; background: var(--green); }
</style>
</head>
<body>
<main class="poster">
  <section class="header">
    <div class="header-photo" role="img" aria-label="Red sharps disposal container with biohazard symbol and open lid"></div>
    <h1 class="motto">PURPOSE<br>CAUSE<br>PASSION</h1>
    <p class="tagline">Remind People What Great<br>Service Looks Like</p>
  </section>

  <section class="values">
    <!-- Teamwork -->
    <svg class="value-icon" style="left:31px;top:28px" viewBox="0 0 82 82">
      <polygon points="41,2 75,21 75,61 41,80 7,61 7,21" fill="var(--green)" stroke="var(--green)" stroke-width="6" stroke-linejoin="round"/>
      <g fill="#fff"><circle cx="41" cy="33" r="7"/><path d="M28 56a13 11 0 0 1 26 0z"/><circle cx="27" cy="37" r="5"/><circle cx="55" cy="37" r="5"/><path d="M17 55a10 9 0 0 1 15-7v7z M65 55a10 9 0 0 0-15-7v7z"/></g>
    </svg>
    <div class="value-title" style="left:32px;top:122px">SYERGY|TEAMWORK</div>
    <div class="value-note" style="left:32px;top:146px">Get it done attitude<br>with humble confidence</div>

    <!-- Safe and secure -->
    <svg class="value-icon" style="left:577px;top:9px" viewBox="0 0 82 82">
      <polygon points="41,2 75,21 75,61 41,80 7,61 7,21" fill="var(--ink)" stroke="var(--ink)" stroke-width="6" stroke-linejoin="round"/>
      <path d="M41 20l16 6v12c0 11-7 19-16 23-9-4-16-12-16-23V26z" fill="none" stroke="#fff" stroke-width="3"/>
      <rect x="35" y="40" width="12" height="9" rx="1" fill="#fff"/><path d="M37 40v-4a4 4 0 0 1 8 0v4" fill="none" stroke="#fff" stroke-width="2.5"/>
    </svg>
    <div class="value-title" style="left:511px;top:100px">SAFE AND SECURE</div>
    <div class="value-note" style="left:514px;top:125px">We are just as secure as an<br>armored truck with money.</div>

    <!-- Core value -->
    <svg class="core-badge" viewBox="0 0 254 280">
      <polygon points="127,10 242,74 242,206 127,270 12,206 12,74" fill="var(--red)" stroke="var(--red)" stroke-width="22" stroke-linejoin="round"/>
    </svg>
    <div class="core-label">CORE<br>VALUE</div>

    <!-- Excellence -->
    <svg class="value-icon" style="left:31px;top:226px" viewBox="0 0 82 82">
      <polygon points="41,2 75,21 75,61 41,80 7,61 7,21" fill="var(--red)" stroke="var(--red)" stroke-width="6" stroke-linejoin="round"/>
      <circle cx="41" cy="34" r="12" fill="none" stroke="#fff" stroke-width="3"/>
      <path d="M35 34l4 4 8-8" fill="none" stroke="#fff" stroke-width="3"/>
      <path d="M33 45l-5 15 6-3 3 6 4-12 4 12 3-6 6 3-5-15" fill="none" stroke="#fff" stroke-width="2.5" stroke-linejoin="round"/>
    </svg>
    <div class="value-title" style="left:34px;top:316px">EXCELLENCE</div>
    <div class="value-note" style="left:34px;top:340px;font-size:11px">Exceed ecpectations with a smile</div>

    <!-- Dependable -->
    <svg class="value-icon" style="left:584px;top:203px" viewBox="0 0 82 82">
      <polygon points="41,2 75,21 75,61 41,80 7,61 7,21" fill="var(--red)" stroke="var(--red)" stroke-width="6" stroke-linejoin="round"/>
      <path d="M18 38l10-9 10 4 7-4 8 1 11 8-13 12c-2 2-5 2-7 0l-10-8" fill="none" stroke="#fff" stroke-width="3" stroke-linejoin="round"/>
      <path d="M30 44l9 8 M34 40l10 9" stroke="#fff" stroke-width="3"/>
    </svg>
    <div class="value-title" style="left:523px;top:300px">DEPENDABLE</div>
    <div class="value-note" style="left:525px;top:328px">Do what you say you will do.</div>

    <!-- Efficient -->
    <svg class="value-icon" style="left:37px;top:394px" viewBox="0 0 82 82">
      <polygon points="41,2 75,21 75,61 41,80 7,61 7,21" fill="var(--ink)" stroke="var(--ink)" stroke-width="6" stroke-linejoin="round"/>
      <circle cx="41" cy="41" r="15" fill="none" stroke="#fff" stroke-width="3" stroke-dasharray="6 3.8"/>
      <circle cx="41" cy="41" r="10" fill="none" stroke="#fff" stroke-width="2.5"/>
      <path d="M41 41l5-5" stroke="#fff" stroke-width="2.5"/>
    </svg>
    <div class="value-title" style="left:40px;top:487px;font-size:23px">EFFICIENT</div>
    <div class="value-note" style="left:40px;top:515px">On-time, sense of urgency,<br>always trying to improve</div>

    <!-- Honesty -->
    <svg class="value-icon" style="left:576px;top:380px" viewBox="0 0 82 82">
      <polygon points="41,2 75,21 75,61 41,80 7,61 7,21" fill="var(--green-bright)" stroke="var(--green-bright)" stroke-width="6" stroke-linejoin="round"/>
      <path d="M41 59C25 48 20 40 20 32a10 10 0 0 1 21-5 10 10 0 0 1 21 5c0 8-5 16-21 27z" fill="#fff"/>
      <path d="M30 40l8 6 6-2" fill="none" stroke="var(--green-bright)" stroke-width="2.5"/>
    </svg>
    <div class="value-title" style="left:519px;top:477px;font-size:19px">HONESTY | INTEGRITY</div>
    <div class="value-note" style="left:521px;top:504px">Do the right thing</div>
  </section>

  <div class="divider"></div>
  <footer class="footer">
    <div class="brand brand-carvobin">CarvoBin</div>
    <div class="brand brand-tidal"><span class="dot"></span>Tidal Pulp</div>
  </footer>
</main>
</body>
</html>
```